Business Card Design for digital storytelling business

I need a business card for a workshop/consulting/coaching business.

Company Name: Bright Harbor Works

Tagline: Modern tools for family stories

What we do: Through workshops, webinars, and coaching we teach you how to capture, tell and share your important memories and stories using readily available digital tools. We will help you tell your life story in a format to share with your family now and in the future.
Updates

I just received a toll free number that I would like included on the designs. If the addition of a phone number would significantly alter your design, please submit an altered version. The number is 866-217-9086

Target Market(s)

Adults in US between ages of 35-70 interested in capturing, preserving and sharing memories and life stories in a digital format.
Could include the following:

-People touched by illness or tragedy who need to tell their own or a loved one's life story
-Grandparents wanting to share stories and wisdom with grandchildren living far away
-People with aging parents who want to capture their stories in a format to pass on to their children
-Alzheimer's patients and their families
-People wanting to transfer analog photos to digital; or wanting to organize digital photos into something that tells a story

Industry/Entity Type

Digital

Requirements
Must have
• Must include business name, logo, tagline

Contact information (see file)
Social media information

Fonts easily readable by aging eyes. Good contrast.

Nice to have
• Color preferences: blue, green, yellow/gold
Blue denotes the calm, non-pressured way that I teach. It is for the healing that comes from telling your story. It represents time and space that are bridged in the digital environment.
Green is for growth, the future, the family tree, Vines that grow and branch and connect the generations and our hearts.
Yellow/gold is for the legacy of wisdom in our lives and stories. It is for the light of truth we bring to the world by sharing our stories.
Should not have
• No old-style, script fonts.
No Times New Roman

```html
<!DOCTYPE html>
<html lang="en">
<head>
<meta charset="utf-8">
<title>Bright Harbor Works — Business Card</title>
<link href="https://fonts.googleapis.com/css2?family=Open+Sans:wght@400;700&family=Lora:wght@400&display=swap" rel="stylesheet">
<style>
  :root {
    --backdrop: #e4e4e2;
    --navy: #1d4873;
    --navy-text: #1c3a63;
    --green: #13894a;
    --gold: #d9a22c;
    --gold-light: #f2c024;
    --gold-deep: #c99328;
    --paper: #fbfbfa;
    --icon-grey: #6b6b6b;
    --tile: #e9e9e9;
  }
  * { margin: 0; padding: 0; box-sizing: border-box; }
  html, body { width: 1200px; height: 720px; overflow: hidden; }
  body {
    background: var(--backdrop);
    position: relative;
    font-family: "Open Sans", Arial, sans-serif;
  }
  .card {
    position: absolute;
    top: 241px;
    width: 420px;
    height: 240px;
    overflow: hidden;
    box-shadow: 0 10px 22px rgba(0,0,0,0.22);
  }
  .brand-name {
    position: absolute;
    font-family: "Open Sans", Arial, sans-serif;
    font-weight: 400;
    color: var(--green);
    white-space: nowrap;
    line-height: 1.2;
  }
  .tagline {
    position: absolute;
    font-family: "Lora", Georgia, serif;
    text-transform: uppercase;
    color: var(--navy-text);
    white-space: nowrap;
    letter-spacing: 0.2px;
    line-height: 1.2;
  }

  /* Front */
  .card--front { left: 147px; background: var(--paper); }
  .front__band {
    position: absolute; left: 0; top: 0; bottom: 0; width: 97px;
    background: var(--navy);
  }
  .front__tile {
    position: absolute; left: 47px; top: 20px; width: 82px; height: 63px;
    background: var(--tile);
  }
  .front__brand { left: 143px; top: 23px; font-size: 24px; }
  .front__tagline { left: 143px; top: 51px; font-size: 9.5px; }
  .person__name {
    position: absolute; left: 142px; top: 71px;
    font-size: 14px; font-weight: 700; color: var(--navy-text); line-height: 1.2;
  }
  .person__role {
    position: absolute; left: 142px; top: 87px;
    font-size: 10px; color: var(--gold-deep); line-height: 1.2;
  }
  .contact-list { list-style: none; position: absolute; left: 141px; top: 106px; }
  .contact-list li {
    display: flex; align-items: center;
    height: 19.5px;
    font-size: 10.5px; color: var(--green);
    white-space: nowrap;
  }
  .contact-list .dot {
    width: 10px; height: 10px; border-radius: 50%;
    background: var(--icon-grey); margin-right: 14px; flex: none;
  }

  /* Back */
  .card--back {
    left: 633px;
    background: radial-gradient(circle at 215px 135px, var(--gold-light) 0%, var(--gold) 45%, var(--gold-deep) 100%);
  }
  .back__tile {
    position: absolute; left: 160px; top: 99px; width: 20px; height: 20px;
    background: var(--navy);
  }
  .back__brand { left: 191px; top: 92px; font-size: 22px; }
  .back__tagline { left: 191px; top: 122px; font-size: 9.5px; }
</style>
</head>
<body>
  <section class="card card--front">
    <div class="front__band"></div>
    <div class="front__tile"></div>
    <div class="brand-name front__brand">Bright Harbor Works</div>
    <div class="tagline front__tagline">Modern tools for family stories</div>
    <div class="person__name">Maren Ellison</div>
    <div class="person__role">Founder</div>
    <ul class="contact-list">
      <li><span class="dot"></span>@BrightHarborW</li>
      <li><span class="dot"></span>www.brightharborworks.com</li>
      <li><span class="dot"></span>maren@brightharborworks.com</li>
      <li><span class="dot"></span>www.snapboard.net/brightharbor</li>
      <li><span class="dot"></span>www.friendsy.net/brightharborworks</li>
      <li><span class="dot"></span>PO Box 218 Millbrook Falls, RI 02911</li>
    </ul>
  </section>

  <section class="card card--back">
    <div class="back__tile"></div>
    <div class="brand-name back__brand">Bright Harbor Works</div>
    <div class="tagline back__tagline">Modern tools for family stories</div>
  </section>
</body>
</html>
```